Consulting Website

We are looking at renewing out company's website. we are an organizational development consulting firm that works within the Middle East and Africa. Our focus on on organizations within the Gulf area.

We are looking to having a simple, clean and attractive website. pictures should be relevant to our location.

We are also looking for a creative design, something that isn't just "another consulting website"
Updates

Thank you all for submitting your designs, following are some general comments;

- Having a veiled women on the intro is NOT a must
- have a picture with people is NOT a must too, we can use nature, symbols, places..anything really!
- Here are some sites i like;
mivanorth.example
http://www.brellokhomes.example/
http://www.quistavarn.example/
http://www.zorebin.example/

I hope these could give you some idea :)

thanks again.

Industry/Entity Type

It Company

Requirements
Must have
• Tabs for press, testimonials, products, resources and services.
pictures also should be relevant to the geographical location. i.e. veiled women, men in traditional costumes and so on.

It's very important that we MAINTAIN the corporate colors of the logo.
Should not have
• Clean and neat design!
i REALLY dont like crowded designs.

```html
<!DOCTYPE html>
<html lang="en">
<head>
<meta charset="utf-8">
<title>Veltrano Consulting</title>
<link rel="stylesheet" href="https://fonts.googleapis.com/css2?family=Stardos+Stencil:wght@700&family=Ubuntu+Condensed&display=swap">
<style>
  :root {
    --stripe-red: #8e1b24;
    --stripe-tan: rgba(224, 168, 120, 0.55);
    --edge-orange: #c8612c;
    --header-tan: #8f7a55;
    --header-text: #fbf3b0;
    --contact-text: #cbbb95;
    --cream: #fbf4bd;
    --about-tile: #f6f3b8;
    --about-ink: #8f7a55;
    --resources-tile: #de2749;
    --products-tile: #22dc0a;
    --services-tile: #e06f0a;
    --press-tile: #a8aa6a;
    --icon-red: #c4313a;
    --panel: rgba(255, 235, 230, 0.22);
    --search-field: rgba(120, 20, 24, 0.75);
    --search-button: #129c10;
    --social-tile: #6c6f8a;
  }
  * { box-sizing: border-box; margin: 0; padding: 0; }
  html, body { width: 1200px; height: 900px; overflow: hidden; }
  body {
    position: relative;
    font-family: "Ubuntu Condensed", "Arial Narrow", sans-serif;
    font-stretch: condensed;
    color: #fff;
    background:
      radial-gradient(ellipse 60% 75% at 50% 45%, rgba(110, 10, 25, 0.55), rgba(0,0,0,0) 70%),
      linear-gradient(90deg, rgba(210,100,40,0.55), rgba(0,0,0,0) 18%, rgba(0,0,0,0) 82%, rgba(210,100,40,0.55)),
      linear-gradient(180deg, rgba(0,0,0,0) 70%, rgba(200,90,40,0.5)),
      repeating-linear-gradient(90deg, var(--stripe-red) 0 20px, var(--stripe-tan) 20px 38px, var(--stripe-red) 38px 62px),
      var(--edge-orange);
  }
  .abs { position: absolute; }
  .stencil { font-family: "Stardos Stencil", "Georgia", serif; font-weight: 700; }

  .site-header {
    left: 52px; top: 0; width: 1100px; height: 130px;
    background: var(--header-tan);
    box-shadow: 0 4px 12px rgba(0,0,0,0.45);
  }
  .contact { left: 12px; top: 2px; color: var(--contact-text); }
  .contact h2 { font-size: 24px; font-weight: 400; letter-spacing: 1px; margin-bottom: 6px; }
  .contact p { font-size: 13px; line-height: 20px; letter-spacing: 0.5px; white-space: nowrap; }
  .brand { right: 20px; top: 16px; text-align: right; color: var(--header-text); }
  .brand .name { font-size: 38px; letter-spacing: 4px; line-height: 44px; }
  .brand .tag { font-size: 34px; letter-spacing: 3px; line-height: 52px; }

  .tab { display: block; text-decoration: none; box-shadow: 0 3px 8px rgba(0,0,0,0.35); }
  .tab-label { position: absolute; font-size: 28px; letter-spacing: 1px; color: var(--cream); white-space: nowrap; }
  .tab-about { left: 52px; top: 130px; width: 162px; height: 175px; background: var(--about-tile); }
  .tab-about .tab-label { left: 25px; bottom: 10px; color: var(--about-ink); }
  .tab-resources { left: 251px; top: 130px; width: 210px; height: 141px; background: var(--resources-tile); }
  .tab-resources .tab-label { left: 12px; bottom: 8px; }
  .tab-products { left: 510px; top: 130px; width: 191px; height: 162px; background: var(--products-tile); }
  .tab-products .tab-label { left: 18px; bottom: 6px; color: #8a9a3a; }
  .tab-services { left: 732px; top: 130px; width: 177px; height: 132px; background: var(--services-tile); }
  .tab-services .tab-label { left: 12px; bottom: 6px; }
  .tab-press { left: 936px; top: 130px; width: 213px; height: 152px; background: var(--press-tile); }
  .tab-press .tab-label { right: 10px; bottom: 10px; text-align: right; line-height: 34px; font-size: 24px; }
  .tab-icon { position: absolute; }
  .icon-placeholder { border-radius: 6px; opacity: 0.8; }

  .intro { left: 58px; top: 342px; width: 205px; font-size: 16px; line-height: 24px; letter-spacing: 0.3px; }
  .text-panel {
    top: 334px; width: 252px; height: 240px;
    background: var(--panel); border-radius: 5px;
    box-shadow: 0 3px 8px rgba(0,0,0,0.4);
    padding: 14px 12px 0 17px;
    font-size: 15px; line-height: 24px; letter-spacing: 0.5px;
    overflow: hidden;
  }
  .photo { border: 3px solid var(--cream); box-shadow: 0 2px 6px rgba(0,0,0,0.4); }
  .photo-courtyard { left: 907px; top: 330px; width: 243px; height: 243px;
    background: linear-gradient(135deg, #e6cfa4, #b89668 55%, #7a5b3a); }

  .work-title { left: 48px; top: 530px; font-size: 34px; letter-spacing: 2px; color: var(--cream); white-space: nowrap; }
  .work-caption { top: 596px; width: 290px; text-align: center; font-size: 27px; line-height: 36px; color: var(--cream); white-space: nowrap; }
  .work-photo { top: 636px; width: 228px; height: 154px; }

  .divider { left: 86px; top: 806px; width: 1017px; height: 3px; background: var(--cream); }

  .search-field { left: 30px; top: 844px; width: 182px; height: 37px; border-radius: 18px; background: var(--search-field); border: none; }
  .search-button { left: 211px; top: 845px; width: 75px; height: 36px; border-radius: 18px; background: var(--search-button); color: var(--cream); font-size: 12px; text-align: center; line-height: 36px; letter-spacing: 0.5px; }

  .social { top: 840px; width: 50px; height: 50px; border-radius: 8px; background: var(--social-tile);
    color: #fff; font-size: 12px; text-align: center; line-height: 50px; text-decoration: none;
    box-shadow: 0 2px 5px rgba(0,0,0,0.4); }
</style>
</head>
<body>

<header class="site-header abs">
  <div class="contact abs">
    <h2>Contact</h2>
    <p>Palm Crest Road, Corvane<br>Hotel, 5th Floor, Office # 402<br>P.O. Box 20418, Dubai, UA<br>Tel: +971 4555 0192</p>
  </div>
  <div class="brand abs stencil">
    <div class="name">VELTRANO</div>
    <div class="tag">CONSULTING</div>
  </div>
</header>

<nav>
  <a class="tab tab-about abs" href="#">
    <svg class="tab-icon" style="left:50px;top:30px" width="50" height="70" viewBox="0 0 50 70" aria-hidden="true">
      <circle cx="32" cy="10" r="7" fill="var(--icon-red)"/>
      <path d="M22 26 L36 26 L26 62 L14 62 Z" fill="var(--icon-red)"/>
    </svg>
    <span class="tab-label stencil">ABOUT</span>
  </a>
  <a class="tab tab-resources abs" href="#">
    <div class="tab-icon icon-placeholder" role="img" aria-label="Cedar tree icon" style="left:68px;top:18px;width:66px;height:72px;background:#f05a78"></div>
    <span class="tab-label stencil">RESOURCES</span>
  </a>
  <a class="tab tab-products abs" href="#">
    <div class="tab-icon icon-placeholder" role="img" aria-label="Puzzle pieces icon" style="left:34px;top:32px;width:96px;height:72px;background:#8fef3c"></div>
    <span class="tab-label stencil">PRODUCTS</span>
  </a>
  <a class="tab tab-services abs" href="#">
    <svg class="tab-icon" style="left:53px;top:22px" width="68" height="68" viewBox="0 0 68 68" aria-hidden="true">
      <circle cx="34" cy="34" r="30" fill="none" stroke="#b58a1a" stroke-width="6"/>
      <circle cx="34" cy="34" r="18" fill="none" stroke="#b58a1a" stroke-width="6"/>
      <circle cx="34" cy="34" r="6" fill="#b58a1a"/>
    </svg>
    <span class="tab-label stencil">SERVICES</span>
  </a>
  <a class="tab tab-press abs" href="#">
    <div class="tab-icon icon-placeholder" role="img" aria-label="Open hand icon" style="left:26px;top:30px;width:56px;height:62px;background:#5fcf2a"></div>
    <span class="tab-label stencil">PRESS<br>TESTIMONIALS</span>
  </a>
</nav>

<p class="intro abs">Veltrano Consulting is one of the first consulting companies in the Middle East and Africa to focus solely on organizational development</p>

<div class="text-panel abs" style="left:316px">text area text area text area text area text area text area text area text area text area text area text area text area text area text area text area text area text area text area text area text area text area text area text area text area text area text area text area</div>
<div class="text-panel abs" style="left:619px">text area text area text area text area text area text area text area text area text area text area text area text area text area text area text area text area text area text area text area text area text area text area text area text area text area text area text area</div>

<div class="photo photo-courtyard abs" role="img" aria-label="Men in traditional dress in an arched courtyard"></div>

<h2 class="work-title abs stencil">OUR WORK</h2>

<span class="work-caption abs" style="left:10px">Organization support</span>
<span class="work-caption abs" style="left:301px">Manage change</span>
<span class="work-caption abs" style="left:602px">Culture transformation</span>
<span class="work-caption abs" style="left:904px">Executive development</span>

<div class="photo work-photo abs" style="left:51px;background:linear-gradient(135deg,#8c9a5a,#3a5bb0 55%,#6b7a3a)" role="img" aria-label="Woman in colourful headscarf outdoors"></div>
<div class="photo work-photo abs" style="left:343px;background:linear-gradient(135deg,#6a3a30,#1a1a1c 50%,#2a2a2e)" role="img" aria-label="Veiled women walking together"></div>
<div class="photo work-photo abs" style="left:636px;background:linear-gradient(135deg,#c8cbd0,#8fa0b4 50%,#6a6a64)" role="img" aria-label="Old town street with traditional doors"></div>
<div class="photo work-photo abs" style="left:929px;background:linear-gradient(135deg,#b04050,#d0b098 50%,#5a3a30)" role="img" aria-label="Men wearing red checked headdresses"></div>

<div class="divider abs"></div>

<input class="search-field abs" type="text" aria-label="Search">
<div class="search-button abs stencil">SEARCH</div>

<a class="social abs" style="left:913px" href="#">Frendly</a>
<a class="social abs" style="left:1007px" href="#">Feedo</a>
<a class="social abs" style="left:1105px" href="#">Linkora</a>

</body>
</html>
```